Need modern simple design for magazine ad, apartment and condo roofer.

I need a half page magazine ad for a local roofer to publish in an industry magazine. Apartment associations industry. All types of roofs. Shingle and Flat
Need the design to be creative and modern, clean and simple. I do not want a busy design. One that stands out and makes a point quickly.
Logo must be prominent.
DO NOT USE PHOTOS FROM MY WEBSITE PLEASE. Looking for something new.
I work on entire complexes not houses.

Need to make sure our phone number and email address are listed at the bottom. Here is my website www.vorbelan.com
Want to stay away from standard clip arts of tools, homes, apartment buildings.
Half Horizontal 7.25 x 4.75
Ads should be in PDF and JPG format.

Target Market(s)

Apartment or Condo owners looking for large scale roofing projects

Industry/Entity Type

Roofing

Requirements
Must have
• Prominent Logo
Simple Clean Design
Create graphics
Not Busy
Should not have
• Clip Art
No Photos from my website

```html
<!DOCTYPE html>
<html lang="en">
<head>
<meta charset="utf-8">
<title>Vorbelan Roofing – Half Page Ad</title>
<link rel="stylesheet" href="https://fonts.googleapis.com/css2?family=Source+Sans+3:wght@600;700&display=swap">
<style>
  :root {
    --brand-blue: #2f82f7;
    --frame-grey: #dfe3e2;
    --line-grey: #8e9995;
    --badge-grey: #d9dedd;
    --badge-dark: #8e9995;
    --slate-light: #a9b3c8;
    --slate-mid: #7a86a3;
    --slate-dark: #3e4862;
    --white: #ffffff;
  }
  * { margin: 0; padding: 0; box-sizing: border-box; }
  html, body { width: 1200px; height: 786px; overflow: hidden; background: var(--white); }
  .ad {
    position: relative;
    width: 1200px;
    height: 786px;
    font-family: "Source Sans 3", Arial, sans-serif;
    background: var(--white);
  }
  .ad-art { position: absolute; inset: 0; }
  .brand {
    position: absolute;
    left: 40px;
    top: 70px;
    display: flex;
    align-items: center;
    gap: 16px;
  }
  .brand-mark {
    width: 40px; height: 40px;
    background: var(--brand-blue);
  }
  .brand-name {
    font-weight: 700;
    font-size: 56px;
    line-height: 1;
    color: var(--brand-blue);
    white-space: nowrap;
  }
  .headline {
    position: absolute;
    left: 50px;
    top: 274px;
    font-weight: 600;
    font-size: 34px;
    line-height: 34px;
    color: var(--brand-blue);
    text-transform: uppercase;
  }
  .experience {
    position: absolute;
    left: 48px;
    top: 604px;
    width: 150px;
    height: 96px;
  }
  .contact {
    position: absolute;
    left: 213px;
    top: 608px;
    color: var(--white);
    font-weight: 600;
    font-style: normal;
  }
  .contact-phone { font-size: 29px; line-height: 34px; }
  .contact-line { font-size: 25px; line-height: 27px; }
</style>
</head>
<body>
<main class="ad">
  <svg class="ad-art" viewBox="0 0 1200 786" width="1200" height="786">
    <defs>
      <linearGradient id="roof-tones" x1="0" y1="0" x2="1" y2="1">
        <stop offset="0" stop-color="#a9b3c8"/>
        <stop offset="0.55" stop-color="#7a86a3"/>
        <stop offset="1" stop-color="#3e4862"/>
      </linearGradient>
    </defs>
    <path class="band" fill="var(--brand-blue)"
      d="M8 412 L410 572 C470 600 505 640 508 700 C510 735 505 760 492 778 L8 778 Z"/>
    <path class="roof-photo" role="img" aria-label="Aerial photo of grey-blue asphalt shingle roofs with gables on a large residential complex"
      fill="url(#roof-tones)"
      d="M668 8 L1192 8 L1192 778 L882 778 L510 505 C430 445 385 400 410 340 Z"/>
    <g class="accent-curves" fill="none" stroke="var(--line-grey)" stroke-width="1.2">
      <path d="M660 8 L402 332 C372 380 395 430 500 510 L885 782"/>
      <path d="M652 8 L392 336 C362 386 388 438 492 516 L872 782"/>
      <path d="M8 392 L420 556 C486 585 520 640 522 702 C523 740 516 765 505 782"/>
      <path d="M8 400 L415 564 C478 594 512 645 514 705 C515 742 508 766 498 782"/>
      <path d="M8 406 L425 560 C500 590 530 650 530 708 C530 745 522 768 512 782"/>
    </g>
    <rect class="frame" x="4" y="4" width="1192" height="778" rx="18" fill="none" stroke="var(--frame-grey)" stroke-width="8"/>
  </svg>

  <div class="brand">
    <span class="brand-mark"></span>
    <span class="brand-name">Vorbelan Roofing</span>
  </div>

  <h1 class="headline">All types of roofs.<br>Shingle and flat</h1>

  <svg class="experience" viewBox="0 0 150 96" aria-label="30+ years experience">
    <text x="0" y="84" font-family="Source Sans 3, Arial, sans-serif" font-weight="700" font-size="104" fill="var(--badge-grey)">3</text>
    <circle cx="97" cy="42" r="36" fill="none" stroke="var(--badge-grey)" stroke-width="10"/>
    <path d="M97 6 A36 36 0 0 0 64 58" fill="none" stroke="var(--badge-dark)" stroke-width="10"/>
    <text x="133" y="16" font-family="Source Sans 3, Arial, sans-serif" font-size="24" fill="var(--white)">+</text>
    <text x="98" y="48" text-anchor="middle" font-family="Source Sans 3, Arial, sans-serif" font-weight="600" font-size="15" fill="var(--white)">YEARS</text>
    <text x="97" y="88" text-anchor="middle" font-family="Source Sans 3, Arial, sans-serif" font-weight="600" font-size="13" fill="var(--white)">EXPERIENCE</text>
  </svg>

  <address class="contact">
    <div class="contact-phone">817.555.0142</div>
    <div class="contact-line">info@vorbelan.com</div>
    <div class="contact-line">www.vorbelan.com</div>
  </address>
</main>
</body>
</html>
```